construction company business card

I need a business card design for a new company called TK BUILDING PARTNERS. I'd like to see different designs with the name tk BUILDING PARTNERS, and others for TK Building Partners. The company field is Home Improvement and everything related with construction. Colors I like are red, blue and black. The final design should communicate/show simplicity and security.

Industry/Entity Type

Construction

Contact Information for Business Card

TK BUILDING PARTNERS
Tobias Kendrick
(555)046-7293
57-31 213th Avenue
Larkfield Hollow
10982, NY

Requirements
Must have
• HOME IMPROVEMENT

```html
<!DOCTYPE html>
<html lang="en">
<head>
<meta charset="utf-8">
<title>TK Building Partners – Business Card</title>
<link rel="stylesheet" href="https://fonts.googleapis.com/css2?family=PT+Sans+Narrow:wght@400;700&display=swap">
<style>
  :root {
    --paper: #76e0fb;
    --paper-shade: #6dd7f2;
    --paper-light: #7fe6ff;
    --fold-line: rgba(40, 150, 190, 0.16);
    --mark-blue: #00c6f8;
    --ink: #0d0d0f;
    --ink-soft: #1c1c20;
  }
  * { margin: 0; padding: 0; box-sizing: border-box; }
  html, body { width: 1200px; height: 683px; overflow: hidden; background: var(--paper); }
  .card {
    position: relative;
    width: 1200px;
    height: 683px;
    overflow: hidden;
    background: var(--paper);
    font-family: "PT Sans Narrow", sans-serif;
  }
  .panel { position: absolute; }
  .panel--top-left {
    left: 0; top: 0; width: 614px; height: 365px;
    background: linear-gradient(180deg, var(--paper-light) 0%, var(--paper) 60%, var(--paper-shade) 100%);
  }
  .panel--top-right {
    left: 614px; top: 0; width: 586px; height: 365px;
    background: linear-gradient(180deg, var(--paper-light) 0%, var(--paper) 70%, var(--paper-shade) 100%);
  }
  .panel--bottom-left {
    left: 0; top: 365px; width: 614px; height: 318px;
    background: linear-gradient(180deg, var(--paper) 0%, var(--paper-light) 100%);
  }
  .panel--bottom-right {
    left: 614px; top: 365px; width: 586px; height: 318px;
    background: linear-gradient(180deg, var(--paper-light) 0%, var(--paper) 100%);
  }
  .fold { position: absolute; background: var(--fold-line); }
  .fold--vertical { left: 613px; top: 0; width: 2px; height: 683px; }
  .fold--horizontal { left: 0; top: 364px; width: 1200px; height: 2px; }

  .brand-square {
    position: absolute;
    left: 945px; top: 235px;
    width: 165px; height: 165px;
    background: var(--mark-blue);
  }

  .contact-block {
    position: absolute;
    right: 230px;
    top: 462px;
    text-align: right;
    color: var(--ink);
  }
  .tagline {
    font-weight: 700;
    font-size: 20px;
    line-height: 1;
    letter-spacing: 3px;
    margin-bottom: 10px;
  }
  .company-name {
    font-weight: 700;
    font-size: 64px;
    line-height: 1;
  }
  .contact-details {
    margin-top: 14px;
    font-weight: 400;
    font-size: 27px;
    line-height: 33px;
    color: var(--ink-soft);
  }
</style>
</head>
<body>
  <main class="card">
    <div class="panel panel--top-left"></div>
    <div class="panel panel--top-right"></div>
    <div class="panel panel--bottom-left"></div>
    <div class="panel panel--bottom-right"></div>
    <div class="fold fold--vertical"></div>
    <div class="fold fold--horizontal"></div>

    <div class="brand-square" aria-hidden="true"></div>

    <section class="contact-block">
      <p class="tagline">HOME IMPROVEMENT</p>
      <h1 class="company-name">TK BUILDING PARTNERS</h1>
      <p class="contact-details">
        TK BUILDING PARTNERS Tobias Kendrick (555)046-7293 57-31<br>
        213th Avenue Larkfield Hollow 10982, NY
      </p>
    </section>
  </main>
</body>
</html>
```